Falvoreth Concert

i need envelope a4 size and normal size - folder -paper bag - business card -
letterhead

Stationery Design project 'Stationery falvoreth concrete : letterhead ,folder,business card ,envelope ,envelope A4size .paper bag '

Target Market(s)

ready mix concrete

Font styles to use
Serif

Colors

Designer to choose colors to be used in the design.

Requirements
Must have
• nice design

```html
<!DOCTYPE html>
<html lang="en">
<head>
<meta charset="utf-8">
<title>Falvoreth For Concrete — Stationery</title>
<link rel="stylesheet" href="https://fonts.googleapis.com/css2?family=Questrial&display=swap">
<style>
  :root {
    --navy: #0b4a7c;
    --paper: #ffffff;
    --paper-shade: #f3f4f6;
    --ground: #e4e5e7;
    --ink: #4a4f56;
    --ink-soft: #7b8088;
    --rule: #d4d7dc;
  }
  * { box-sizing: border-box; margin: 0; padding: 0; }
  html, body { width: 1200px; height: 479px; overflow: hidden; }
  body {
    background: var(--ground);
    font-family: "Questrial", "Century Gothic", sans-serif;
    color: var(--ink);
    position: relative;
  }
  .sheet { position: absolute; background: var(--paper); box-shadow: 0 1px 3px rgba(0,0,0,.12); overflow: hidden; }

  /* wordmark used in place of the mark */
  .wordmark { display: flex; align-items: center; gap: 4px; color: var(--navy); text-transform: uppercase; letter-spacing: .02em; line-height: 1.1; }
  .wordmark__dot { width: 7px; height: 7px; border-radius: 50%; background: currentColor; flex: none; }
  .wordmark--light { color: #fff; }

  /* letterhead */
  .letterhead { left: 44px; top: 56px; width: 268px; height: 376px; }
  .letterhead .wordmark { position: absolute; left: 24px; top: 34px; font-size: 6.5px; width: 70px; }
  .letterhead__contact { position: absolute; left: 194px; top: 33px; border-left: 1px solid var(--navy); padding-left: 5px; font-size: 3.8px; line-height: 1.45; color: var(--navy); }
  .letterhead__body { position: absolute; left: 24px; top: 104px; width: 222px; }
  .letterhead__greeting { font-size: 6.4px; margin-bottom: 10px; }
  .letterhead__body p { font-size: 3.6px; line-height: 1.7; color: var(--ink-soft); margin-bottom: 6px; }
  .letterhead__signature { width: 48px; height: 18px; background: #c9d6e8; margin-top: 4px; }

  /* envelopes */
  .envelope-a4 { left: 332px; top: 64px; width: 238px; height: 368px; }
  .flap { position: absolute; left: 0; right: 0; top: 0; background: var(--navy); border-radius: 0 0 10px 10px; }
  .envelope-a4 .flap { height: 32px; border-radius: 10px 10px 0 0; }
  .envelope-a4 .wordmark { position: absolute; left: 14px; top: 50px; font-size: 5.5px; width: 70px; }
  .return-address { position: absolute; font-size: 3.8px; line-height: 1.4; color: var(--ink); }
  .envelope-a4 .return-address { left: 14px; top: 80px; }

  .envelope-dl-back { left: 514px; top: 150px; width: 308px; height: 140px; background: var(--paper-shade); }
  .envelope-dl-back .flap { height: 36px; border-radius: 0 0 16px 16px; }
  .envelope-dl-back__tag { position: absolute; top: 44px; width: 100%; text-align: center; color: var(--navy); }
  .envelope-dl-back__tag .name { font-size: 6px; text-transform: uppercase; }
  .envelope-dl-back__tag .web { font-size: 4px; letter-spacing: .3em; margin-top: 3px; }

  .envelope-dl-front { left: 415px; top: 226px; width: 309px; height: 141px; }
  .envelope-dl-front .wordmark { position: absolute; left: 16px; top: 18px; font-size: 5.5px; width: 70px; }
  .envelope-dl-front .return-address { left: 16px; top: 48px; }

  /* business cards */
  .card { top: 70px; height: 63px; }
  .card-front { left: 586px; width: 118px; background: var(--paper-shade); }
  .card-front .wordmark { position: absolute; left: 8px; top: 20px; font-size: 4.6px; width: 48px; }
  .card-front__details { position: absolute; left: 62px; top: 11px; border-left: 1px solid var(--rule); padding-left: 4px; font-size: 3px; line-height: 1.45; color: var(--ink); }
  .card-front__name { color: var(--navy); font-size: 4.2px; text-transform: uppercase; }
  .card-back { left: 710px; width: 112px; background: var(--navy); }
  .card-back .wordmark { position: absolute; left: 0; right: 0; top: 20px; justify-content: center; font-size: 5px; }
  .card-back__web { position: absolute; bottom: 5px; width: 100%; text-align: center; font-size: 3px; letter-spacing: .3em; color: #c6d4e4; }

  /* paper bag */
  .bag { position: absolute; left: 745px; top: 340px; width: 84px; height: 98px; background: #1d4868; }
  .bag__handle { position: absolute; top: -20px; width: 28px; height: 28px; border: 1.5px solid #1d4868; border-bottom: none; border-radius: 14px 14px 0 0; }
  .bag__handle--left { left: 10px; }
  .bag__handle--right { left: 46px; }
  .bag .wordmark { position: absolute; left: 8px; top: 36px; font-size: 4.6px; width: 60px; }

  /* folder */
  .folder { position: absolute; left: 847px; top: 32px; width: 155px; height: 401px; background: var(--navy); box-shadow: -3px 0 0 #0a4270, -6px 0 0 #0d4f84; }
  .folder .wordmark { position: absolute; left: 14px; right: 10px; top: 186px; font-size: 9px; flex-direction: column; align-items: flex-start; gap: 6px; }
  .folder .wordmark__dot { width: 12px; height: 12px; }
</style>
</head>
<body>

  <!-- Letterhead -->
  <article class="sheet letterhead">
    <div class="wordmark"><span class="wordmark__dot"></span><span>Falvoreth For Concrete</span></div>
    <div class="letterhead__contact">
      4210 Larkspur Road<br>Juneau, Alaska 99801<br>&#9742; 555 014 2290<br>&#9993; elias@falvoreth.com<br>&#9679; www.falvoreth.com
    </div>
    <div class="letterhead__body">
      <p class="letterhead__greeting">Dear Mr. Brandt,</p>
      <p>We are pleased to confirm the delivery schedule for your ready mix concrete order. Our plant team will coordinate each pour with your site manager to keep work on time and within budget.</p>
      <p>All batches are tested at our laboratory before dispatch. Slump, strength and temperature records will be sent with every truck so your engineers can review them on arrival.</p>
      <p>Should the site require pumping, additives or weekend deliveries, please let us know two days in advance. We will gladly adjust the mix design to suit the weather and the structure.</p>
      <p>Thank you for choosing us as your concrete partner. We look forward to building a strong project together.</p>
      <p>Sincerely,</p>
      <div class="letterhead__signature" role="img" aria-label="Handwritten signature of Elias Brandt"></div>
    </div>
  </article>

  <!-- A4 envelope -->
  <article class="sheet envelope-a4">
    <div class="flap"></div>
    <div class="wordmark"><span class="wordmark__dot"></span><span>Falvoreth For Concrete</span></div>
    <div class="return-address">4210 Larkspur Road<br>Juneau, Alaska 99801</div>
  </article>

  <!-- Business cards -->
  <article class="sheet card card-front">
    <div class="wordmark"><span class="wordmark__dot"></span><span>Falvoreth For Concrete</span></div>
    <div class="card-front__details">
      <div class="card-front__name">Elias Brandt</div>
      CEO/Founder<br>4210 Larkspur Road<br>Juneau, Alaska 99801<br>&#9742; 555 014 2290<br>&#9742; 555 014 2291<br>&#9742; 555 014 2292<br>&#9993; elias@falvoreth.com<br>&#9679; www.falvoreth.com
    </div>
  </article>
  <article class="sheet card card-back">
    <div class="wordmark wordmark--light"><span>Falvoreth For Concrete</span></div>
    <div class="card-back__web">www.falvoreth.com</div>
  </article>

  <!-- DL envelope, back -->
  <article class="sheet envelope-dl-back">
    <div class="flap"></div>
    <div class="envelope-dl-back__tag">
      <div class="name">Falvoreth For Concrete</div>
      <div class="web">www.falvoreth.com</div>
    </div>
  </article>

  <!-- DL envelope, front -->
  <article class="sheet envelope-dl-front">
    <div class="wordmark"><span class="wordmark__dot"></span><span>Falvoreth For Concrete</span></div>
    <div class="return-address">4210 Larkspur Road<br>Juneau, Alaska 99801</div>
  </article>

  <!-- Paper bag -->
  <article class="bag">
    <span class="bag__handle bag__handle--left"></span>
    <span class="bag__handle bag__handle--right"></span>
    <div class="wordmark wordmark--light"><span>Falvoreth For Concrete</span></div>
  </article>

  <!-- Folder -->
  <article class="folder">
    <div class="wordmark wordmark--light"><span class="wordmark__dot"></span><span>Falvoreth For Concrete</span></div>
  </article>

</body>
</html>
```